Business Design for Printed Shipping Tape

We need a company logo design to be printed on packaging natural color WAT tape for shipping boxes. www.brightmeadowkelp.com
The tape is 3" wide. Repeat pattern every 10 inches.
Would like our website vertical at one end side and "The Future of Nutrition" on the opposite end.

Industry/Entity Type

Health, Nutrition

Font styles to use
Sans Serif

Requirements
Must have
• Company Logo (attached) website and text "The Future of Nutrition"
Nice to have
• Tape is Natural Color.

```html
<!DOCTYPE html>
<html lang="en">
<head>
<meta charset="utf-8">
<title>Bright Meadow Kelp – Shipping Tape</title>
<link href="https://fonts.googleapis.com/css2?family=Montserrat:wght@700&family=Raleway:wght@400;500&display=swap" rel="stylesheet">
<style>
  :root {
    --backdrop: #5a5a5a;
    --tape: #ffffff;
    --ink: #232323;
    --green: #1f6a47;
    --photo-green: #5f8a5a;
    --photo-blue: #8cc4e2;
    --photo-light: #e4f1f8;
  }
  html, body {
    margin: 0;
    padding: 0;
    width: 1200px;
    height: 3075px;
    overflow: hidden;
    background: var(--backdrop);
  }
  .canvas {
    position: relative;
    width: 1200px;
    height: 3075px;
  }
  .tape-strip {
    position: absolute;
    left: 50px;
    top: 1372px;
    width: 1100px;
    height: 330px;
    background: var(--tape);
    box-shadow: 0 10px 30px rgba(0,0,0,0.25);
  }
  .end-note {
    position: absolute;
    top: 0;
    height: 330px;
    margin: 0;
    writing-mode: vertical-rl;
    text-align: center;
    font-family: "Raleway", sans-serif;
    font-weight: 500;
    font-size: 17px;
    letter-spacing: 0.5px;
    color: var(--green);
  }
  .website { left: 18px; transform: rotate(180deg); }
  .future-tagline { right: 18px; }
  .brand-name {
    position: absolute;
    left: 70px;
    top: 120px;
    width: 260px;
    margin: 0;
    font-family: "Montserrat", sans-serif;
    font-weight: 700;
    font-size: 36px;
    line-height: 1.15;
    color: var(--ink);
    text-align: center;
  }
  .product-photo {
    position: absolute;
    left: 350px;
    top: 30px;
    width: 370px;
    height: 270px;
    background: linear-gradient(180deg, var(--photo-light) 0%, var(--photo-green) 45%, var(--photo-blue) 80%, var(--photo-light) 100%);
  }
  .claims {
    position: absolute;
    left: 748px;
    top: 108px;
    font-family: "Raleway", sans-serif;
    color: var(--green);
    font-size: 25px;
    line-height: 1.22;
  }
  .claims p { margin: 0; }
  .claims .lead { font-weight: 400; margin-bottom: 6px; }
  .claims .highlight { font-weight: 500; }
</style>
</head>
<body>
  <main class="canvas">
    <section class="tape-strip" aria-label="Shipping tape repeat">
      <p class="end-note website">www.brightmeadowkelp.com</p>
      <h1 class="brand-name">BRIGHT MEADOW<br>KELP</h1>
      <div class="product-photo" role="img" aria-label="Photo of a jar of green superfood powder in a water splash"></div>
      <div class="claims">
        <p class="lead">Experience something<br>completely different</p>
        <p class="highlight">World’s Most<br>Powerful Superfood</p>
      </div>
      <p class="end-note future-tagline">The Future of Nutrition</p>
    </section>
  </main>
</body>
</html>
```